Time for a new business card design

We need a new business card design for Torvel Furniture Rentals based in Australia. www.torvel-example.com.au. We specialise in providing furniture rentals for home staging, corporate relocations events and product launches etc. We would like to see designs that include our logo on the front of the card with all the standard contact details as well as having a realy nice image on the back with a list of our services we offer. Our logo is red and this cannot change. Were looking for a pallet of red and white with maybe a splash of grey. The final design should communication organised & stylish. We are in the process of finalising our new website and would like the card design to compliment this as well

Industry/Entity Type

Communication

Requirements
Must have
• Square corners
logo
name, title, email, phone, address
image on back of card with space for list of services we offer
Services:
•Furniture and appliance rental
•Property styling
•Events and functions
•Office furniture rental

The card must be landscape.
The image is to appear on the back of the card only.

```html
<!DOCTYPE html>
<html lang="en">
<head>
<meta charset="utf-8">
<title>Torvel Furniture Rentals – Business Card</title>
<link href="https://fonts.googleapis.com/css2?family=Questrial&family=Arimo:wght@700&display=swap" rel="stylesheet">
<style>
  :root {
    --brand-red: #b0121e;
    --deep-red: #9a0f19;
    --soft-red: #e8505c;
    --pale-red: #f4a3aa;
    --white: #ffffff;
    --ink: #3a3a3a;
    --backdrop: #ecebe8;
  }
  * { margin: 0; padding: 0; box-sizing: border-box; }
  html, body {
    width: 1200px; height: 1000px; overflow: hidden;
    background: var(--backdrop);
    font-family: "Questrial", Arial, sans-serif;
  }
  .canvas { position: relative; width: 1200px; height: 1000px; }

  .card {
    position: absolute; width: 749px; height: 444px; overflow: hidden;
    box-shadow: 0 6px 18px rgba(0,0,0,.18);
  }
  .card svg.card-art { position: absolute; inset: 0; width: 100%; height: 100%; }

  /* Back of card */
  .card-back { left: 71px; top: 29px; background: var(--brand-red); }
  .card-back .wordmark {
    position: absolute; left: 140px; top: 70px;
    color: var(--white); font-size: 46px; letter-spacing: -0.5px; white-space: nowrap;
  }
  .services {
    position: absolute; left: 0; right: 0; bottom: 0; height: 52px;
    display: flex; align-items: center; justify-content: center; gap: 8px;
    list-style: none; color: var(--white); white-space: nowrap;
    font-family: "Arimo", Arial, sans-serif; font-weight: 700; font-size: 15px;
  }
  .services li + li::before {
    content: ""; display: inline-block; width: 5px; height: 5px;
    background: #1a1a1a; margin-right: 8px; vertical-align: middle;
  }

  /* Front of card */
  .card-front { left: 393px; top: 511px; background: var(--white); }
  .card-front .wordmark {
    position: absolute; left: 38px; top: 40px;
    color: var(--brand-red); font-size: 46px; letter-spacing: -0.5px; white-space: nowrap;
  }
  .person { position: absolute; left: 440px; top: 148px; }
  .person-name { color: var(--brand-red); font-size: 32px; font-weight: 400; }
  .person-title { color: #555; font-size: 20px; margin-left: 115px; margin-top: 2px; }
  .contact { position: absolute; left: 38px; top: 203px; color: var(--ink); font-size: 19px; line-height: 1.2; white-space: nowrap; }
  .contact address { font-style: normal; margin-left: 4px; }
  .contact-row { display: flex; align-items: center; gap: 6px; }
  .contact-row svg { width: 18px; height: 18px; flex: none; }
  .contact-row.phone { margin-top: 9px; }
  .contact-row.email { margin-top: 13px; }
  .contact-row.web { margin-top: 2px; }
</style>
</head>
<body>
<main class="canvas">

  <section class="card card-back" aria-label="Back of card">
    <svg class="card-art" viewBox="0 0 749 444" preserveAspectRatio="none">
      <defs>
        <linearGradient id="roomTones" x1="0" y1="0" x2="1" y2="1">
          <stop offset="0" stop-color="#dfe3e6"/>
          <stop offset="0.45" stop-color="#f2f2f0"/>
          <stop offset="0.7" stop-color="#9fc4e0"/>
          <stop offset="1" stop-color="#c9a488"/>
        </linearGradient>
      </defs>
      <path role="img" aria-label="Photo of a styled bright living room with cushions, lamp and ocean view"
            d="M0 150 C150 230 350 255 500 205 C620 165 700 150 749 175 L749 392 L0 392 Z"
            fill="url(#roomTones)"/>
      <path d="M0 175 C160 255 360 270 510 222 C630 185 700 170 749 190" fill="none" stroke="rgba(255,255,255,.55)" stroke-width="3"/>
      <path d="M0 195 C170 275 370 285 520 238 C640 200 705 188 749 205" fill="none" stroke="rgba(255,255,255,.35)" stroke-width="2"/>
    </svg>
    <div class="wordmark">Torvel Furniture Rentals</div>
    <ul class="services">
      <li>Furniture and appliance rental</li>
      <li>Property styling</li>
      <li>Events and functions</li>
      <li>Office furniture rental</li>
    </ul>
  </section>

  <section class="card card-front" aria-label="Front of card">
    <svg class="card-art" viewBox="0 0 749 444" preserveAspectRatio="none" aria-hidden="true">
      <path d="M0 358 C160 325 330 345 470 368 C600 390 690 375 749 350 L749 444 L0 444 Z" fill="var(--pale-red)"/>
      <path d="M0 368 C170 340 340 360 480 382 C610 400 695 385 749 362 L749 444 L0 444 Z" fill="var(--soft-red)"/>
      <path d="M0 382 C180 360 350 380 490 398 C620 414 700 400 749 380 L749 444 L0 444 Z" fill="var(--brand-red)"/>
      <path d="M0 410 C200 398 370 412 520 424 C640 432 710 420 749 408 L749 444 L0 444 Z" fill="var(--deep-red)"/>
    </svg>
    <div class="wordmark">Torvel Furniture Rentals</div>

    <div class="person">
      <h1 class="person-name">Name</h1>
      <p class="person-title">Designation</p>
    </div>

    <div class="contact">
      <address>2718 Sample Street West<br>Northvale, NV 60912</address>
      <p class="contact-row phone">
        <svg viewBox="0 0 24 24" aria-hidden="true"><path fill="var(--brand-red)" d="M6.6 10.8a15.1 15.1 0 0 0 6.6 6.6l2.2-2.2c.3-.3.7-.4 1-.2 1.1.4 2.3.6 3.6.6.6 0 1 .4 1 1V20c0 .6-.4 1-1 1A17 17 0 0 1 3 4c0-.6.4-1 1-1h3.5c.6 0 1 .4 1 1 0 1.3.2 2.5.6 3.6.1.3 0 .7-.2 1z"/></svg>
        1800 555 010 (free call)
      </p>
      <p class="contact-row email">
        <svg viewBox="0 0 24 24" aria-hidden="true"><rect x="2" y="5" width="20" height="14" rx="2" fill="var(--brand-red)"/><path d="M3 7l9 6 9-6" fill="none" stroke="#fff" stroke-width="1.8"/></svg>
        name@torvel-example.com.au
      </p>
      <p class="contact-row web">
        <svg viewBox="0 0 24 24" aria-hidden="true"><g fill="none" stroke="var(--brand-red)" stroke-width="2"><circle cx="12" cy="12" r="9"/><ellipse cx="12" cy="12" rx="4" ry="9"/><path d="M3 12h18M5 7h14M5 17h14"/></g></svg>
        www.torvel-example.com.au
      </p>
    </div>
  </section>

</main>
</body>
</html>
```